Business cards, letter head, stationery
trial lawyer
Bright & Fun-filled
Teodoro Villaseca
Trial Lawyer
2716 kelverham, suite 300
Bellaire Texas 77538
Tevmilux@quarnela.com
Need to include:
Offices in Houston , San Antonio, and eagle pass Texas
Use winning logo

```html
<!DOCTYPE html>
<html lang="en">
<head>
<meta charset="utf-8">
<title>Teodoro Villaseca — Business Cards</title>
<link href="https://fonts.googleapis.com/css2?family=Crimson+Text:wght@400;600;700&display=swap" rel="stylesheet">
<style>
  :root{
    --bg:#e4e6ea;
    --navy:#1d3f7a;
    --navy-deep:#122a57;
    --blue-bright:#2d63b3;
    --orange:#f26b1d;
    --orange-light:#ff9a3c;
    --white:#ffffff;
    --ink:#24324f;
    --grey-card:#f1f2f4;
  }
  *{margin:0;padding:0;box-sizing:border-box}
  html,body{width:1200px;height:875px;overflow:hidden;background:var(--bg)}
  body{position:relative;font-family:"Crimson Text",Georgia,serif}
  .card{
    position:absolute;width:460px;height:262px;border-radius:16px;overflow:hidden;
    box-shadow:0 6px 18px rgba(0,0,0,.22);
  }
  .card--front{left:110px;top:190px;background:var(--white)}
  .card--navy{left:640px;top:120px;background:linear-gradient(135deg,var(--blue-bright) 0%,var(--navy) 55%,var(--navy-deep) 100%)}
  .card--orange{left:100px;top:480px;background:linear-gradient(135deg,var(--orange-light) 0%,var(--orange) 60%,#e0560f 100%)}
  .card--white{left:640px;top:440px;background:linear-gradient(135deg,var(--white) 0%,var(--grey-card) 100%)}

  .swoosh{position:absolute;inset:0;width:100%;height:100%}

  .brand{position:absolute;display:flex;align-items:center;gap:10px}
  .brand__mark{width:30px;height:30px;flex:none}
  .brand__name{font-size:24px;font-weight:600;letter-spacing:1px;text-transform:uppercase;white-space:nowrap}
  .brand--dark .brand__mark{background:var(--navy)}
  .brand--dark .brand__name{color:var(--navy)}
  .brand--light .brand__mark{background:var(--white)}
  .brand--light .brand__name{color:var(--white)}

  .card--front .brand{left:24px;top:40px}
  .card--front .brand__name{font-size:21px}
  .card--navy .brand,.card--orange .brand,.card--white .brand{left:50%;top:78px;transform:translateX(-50%)}

  .person{position:absolute;left:218px;top:118px;color:var(--orange);font-size:20px;font-weight:700;white-space:nowrap}

  .contact{position:absolute;left:24px;top:110px;font-size:11px;line-height:15px;color:var(--ink)}
  .contact__row{display:flex;gap:8px}
  .contact__label{width:34px;color:var(--orange);font-weight:700}

  .offices{position:absolute;left:50%;top:160px;transform:translateX(-50%);text-align:center;font-size:12.5px;line-height:16px;white-space:nowrap}
  .offices__title{font-weight:700}
  .offices--light{color:var(--white)}
  .offices--dark{color:var(--navy)}
</style>
</head>
<body>

  <section class="card card--front">
    <svg class="swoosh" viewBox="0 0 460 262" preserveAspectRatio="none" aria-hidden="true">
      <path d="M345 0 Q455 120 385 262 L460 262 L460 0 Z" fill="var(--orange)"/>
      <path d="M365 0 Q475 120 405 262 L460 262 L460 0 Z" fill="var(--navy)"/>
    </svg>
    <div class="brand brand--dark">
      <span class="brand__mark"></span>
      <span class="brand__name">Teodoro Villaseca</span>
    </div>
    <p class="person">Marisol Quenby</p>
    <div class="contact">
      <p>2716 kelverham, suite 300</p>
      <p>Bellaire Texas 77538</p>
      <p class="contact__row"><span class="contact__label">Phone</span><span>713-555-0142</span></p>
      <p class="contact__row"><span class="contact__label">Cell</span><span>713-555-0187</span></p>
      <p class="contact__row"><span class="contact__label">Fax</span><span>713-555-0163</span></p>
      <p class="contact__row"><span class="contact__label">Email</span><span>Tevmilux@quarnela.com</span></p>
      <p class="contact__row"><span class="contact__label">Web</span><span>pivot8181.com</span></p>
    </div>
  </section>

  <section class="card card--navy">
    <div class="brand brand--light">
      <span class="brand__mark"></span>
      <span class="brand__name">Teodoro Villaseca</span>
    </div>
    <div class="offices offices--light">
      <p class="offices__title">Satellite offices in San Antonio</p>
      <p>8450 Calloway Rd. Suite 210</p>
      <p>San Antonio Texas 78249</p>
    </div>
  </section>

  <section class="card card--orange">
    <div class="brand brand--light">
      <span class="brand__mark"></span>
      <span class="brand__name">Teodoro Villaseca</span>
    </div>
    <div class="offices offices--light">
      <p class="offices__title">Satellite offices in San Antonio</p>
      <p>8450 Calloway Rd. Suite 210</p>
      <p>San Antonio Texas 78249</p>
    </div>
  </section>

  <section class="card card--white">
    <div class="brand brand--dark">
      <span class="brand__mark"></span>
      <span class="brand__name">Teodoro Villaseca</span>
    </div>
    <div class="offices offices--dark">
      <p class="offices__title">Satellite offices in San Antonio</p>
      <p>8450 Calloway Rd. Suite 210</p>
      <p>San Antonio Texas 78249</p>
    </div>
  </section>

</body>
</html>
```